Infographic for law firm in criminal cases

We would like an infographic created for our law firm. We would like to highlight the information below in a more interesting, eye-catching and engaging way. There are 3 buckets of information numbered below. The numbers in bucket 1 will be updated once we receive the 2016 ones on Jan 2nd but please use these 2013 numbers as placeholders. In 2 and 3 we'd like pictures as well but very tasteful and not cartoony. Feel free to tweak text as needed but keep to the message. Since this is a law firm and serious issue, we would like the overall tone and color scheme to be appropriate as to that.

1. Total Number of DWI Arrests in Marlow Parish

The Marlow Parish District Attorney's Office has reported 7,649 total DWI arrests in 2013. Of the total number of arrests, 3,364 involved a blood draw. In 2013, arrests were made for the following types of DWI related offenses as follows:

5,637 arrests for a first DWI offense (including charges for a 1st DWI, open container DWI, and DWI with a BAC of .15 or greater);
1,105 arrests for a second DWI offense;
703 arrests for a third or subsequent DWI offense;
152 arrests for any DWI with a child passenger under the age of 15 years old;
37 arrests for a charge of intoxication assault;
15 arrests for intoxication manslaughter
*information obtained from the Marlow Parish District Attorney's Office

2. If you are found guilty of a DWI and you do not choose a lawyer with experience, your life can be affected with one or more of the following:
- Permanent criminal record which could impact your current and future employment.
- A driver’s license suspension from 6 months to 2 years on average.
- High fines amounts you will be required to pay based on your own case details.
- Installation of an Ignition Interlock Device system in your vehicle for an average of 1 to 3 years at your expense.
- Requirement to take DUI classes and/or counseling before any drivers license reinstatement.
- Possible requirement to pay much higher insurance rates, or lose your coverage entirely.
- Possible travel restrictions
- Community service
- Social stigma and hardships on family and friends

3. Hiring a quality criminal defense lawyer is probably the single most important decision you can make. Things to take into consideration when selecting your attorney:

- Experience. DWI law is always changing,

- Local. it's important that the attorney have experience in the city or county where the arrest took place.

- Fair fee.

Please include the law firm's name and phone number somewhere very visible and eye-catching in the infographic:

Brandt & Okafor Law
555-013-7200

We can send you their logo if it fits, it is a compass. Feel free to put something like call to speak to an experienced attorney now. The sooner you call, the sooner we can help: 555-013-7200. If you think an email is helpful their email is office@brandt-okafor.example

Possible title examples:
Former Prosecutors Fighting for You
DWI Battle? Have Prosecutors on Your Side
DWI Arrest? Fight Back

Some infographic examples that we like:

https://blog.tallyprism.example/12-infographic-tips/

We love images that show power without feeling like advertisement. Images that are thoughtful and tell a story but tasteful for example velmont's recent campaign:

https://mobile.chirpnet.example/Velmont/status/503821947716208351?ref_src=src%5Esearch%7Ccamp%5Eresults%7Cgr%5Epost

Thanks!
Dana

Industry/Entity Type

Legal

Requirements
Must have
• Must fit in 8 X 10 sheet of paper
Nice to have
• Logo. I attached word document with logo at the top. Not sure if it will fit.

```html
<!DOCTYPE html>
<html lang="en">
<head>
<meta charset="utf-8">
<title>DWI Arrest? Fight Back — Brandt &amp; Okafor</title>
<link rel="stylesheet" href="https://fonts.googleapis.com/css2?family=Open+Sans:wght@400;600;700;800&family=Roboto+Condensed:wght@400;700&display=swap">
<style>
  :root{
    --gold:#f4ae14;
    --gold-deep:#d9950a;
    --brown:#5a3a26;
    --brown-dark:#2a1a11;
    --ink:#1f1f1f;
    --grey:#6e6e6e;
    --paper:#f1f1f1;
    --white:#ffffff;
    --night:#141210;
  }
  *{box-sizing:border-box;margin:0;padding:0}
  html,body{width:993px;height:1200px;overflow:hidden;background:var(--white)}
  body{font-family:"Open Sans",Arial,sans-serif;color:var(--ink);position:relative}
  .sheet{position:absolute;left:77px;top:92px;width:838px;height:1016px;box-shadow:0 0 6px rgba(0,0,0,.25);overflow:hidden}
  .abs{position:absolute}

  /* ---------- statistics band ---------- */
  .stats{position:absolute;left:0;top:0;width:838px;height:472px;
    background:linear-gradient(180deg,#3b2a21 0%,#6a4a36 45%,#5b3b27 70%,#3a2416 100%)}
  .stats__photo{position:absolute;left:0;top:0;width:838px;height:300px;
    background:radial-gradient(ellipse at 50% 40%,rgba(210,170,140,.35),rgba(0,0,0,0) 65%)}
  .title{left:0;width:838px;text-align:center;color:var(--white);font-weight:800;line-height:1;text-shadow:0 2px 4px rgba(0,0,0,.4)}
  .title--main{top:28px;font-size:63px;color:#e9e9e9}
  .title--sub{top:92px;font-size:47px}
  .county{left:0;top:188px}
  .county__heading{left:33px;top:196px;width:215px;font-size:23px;font-weight:800;line-height:1.08;color:var(--ink)}
  .big{font-size:32px;font-weight:800;color:var(--white);line-height:1}
  .label{font-size:14px;color:var(--white);line-height:1.12}
  .label b{font-weight:800}
  .muted{font-size:13px;font-weight:700;color:#7a5a2a;line-height:1.1}
  .art{left:122px;top:374px;width:108px;height:56px;background:linear-gradient(135deg,#2b2b2b,#6a4b1c);border-radius:6px}
  .source{left:33px;top:438px;width:88px;font-size:7.5px;color:#6a4a1a;line-height:1.2}
  .asterisk{left:232px;top:440px;width:80px;font-size:7.5px;color:#f3e7d6;line-height:1.2}
  .intro{left:350px;top:262px;width:190px;font-size:13px;color:#f0e4d6;line-height:1.2}
  .intro b{font-size:19px;font-weight:800;color:var(--white)}
  .intro strong{font-weight:700;color:var(--white)}
  .divider{left:553px;top:255px;width:1px;height:192px;background:rgba(244,174,20,.6)}
  .badge{width:46px;height:46px;border-radius:50%;border:4px solid rgba(255,255,255,.45);
    display:flex;flex-direction:column;align-items:center;justify-content:center;color:#cfc2b5;font-size:7px;line-height:1}
  .badge b{font-size:13px;font-weight:600;color:#e5dbd0;margin:1px 0}
  .stat{font-size:12.5px;font-weight:600;color:var(--gold);line-height:1.15}
  .stat b{font-size:17px;font-weight:800;color:var(--white)}
  .stat small{display:block;font-size:9.5px;font-weight:400;color:#d8c6b2;margin-top:2px;line-height:1.25}

  /* ---------- consequences band ---------- */
  .effects{position:absolute;left:0;top:472px;width:838px;height:311px;background:linear-gradient(180deg,#fafafa,#e6e6e6)}
  .effects__heading{left:33px;top:18px;width:490px;font-size:23px;font-weight:800;line-height:1.1;color:var(--ink)}
  .effects__heading span{color:var(--grey)}
  .gavel{left:560px;top:18px;width:205px;height:78px;background:linear-gradient(135deg,#e8e8e8,#f4ae14 70%,#1b1b1b);border-radius:4px;opacity:.9}
  .item{display:flex;align-items:flex-start;gap:8px;padding:0 8px 8px 0;border-right:2px solid var(--gold);border-bottom:2px solid var(--gold);height:76px;
    font-family:"Roboto Condensed","Arial Narrow",sans-serif;font-size:13px;line-height:1.12;color:var(--grey)}
  .item p{flex:1}
  .item b{color:var(--ink)}
  .icon{flex:none;width:36px;height:36px;margin-top:14px}

  /* ---------- call-to-action band ---------- */
  .cta{position:absolute;left:0;top:783px;width:838px;height:233px;background:linear-gradient(90deg,#1d1612 0%,#3b2b1e 40%,#0d0c0b 70%,#2a2624 100%)}
  .cta__photo{left:250px;top:0;width:588px;height:233px;background:radial-gradient(ellipse at 80% 40%,rgba(120,110,100,.35),rgba(0,0,0,0) 60%)}
  .cta__headline{left:33px;top:30px;width:260px;font-size:19px;font-weight:700;line-height:1.24;color:var(--white)}
  .cta__headline strong{font-weight:800}
  .logo{left:33px;top:170px;display:flex;align-items:center;gap:10px;font-size:19px;font-weight:600;color:#e8e8e8;letter-spacing:.5px}
  .logo i{width:30px;height:30px;border:2px solid #e8e8e8;border-radius:50%}
  .point{left:354px;width:206px;height:52px;background:linear-gradient(90deg,rgba(244,174,20,.55),var(--gold) 35%);
    display:flex;align-items:center;gap:12px;padding-left:12px;color:var(--white);font-weight:800;font-size:17px;line-height:1.05}
  .point svg{flex:none}
  .call{left:575px;top:32px;width:165px;font-size:15px;color:#e6e6e6;line-height:1.3}
  .call b{color:var(--white);font-weight:700}
  .phone{left:575px;top:156px;font-size:30px;font-weight:800;color:var(--gold);line-height:1.2}
  .email{left:575px;top:199px;width:250px;font-size:16px;font-weight:600;color:var(--gold);line-height:1.2;white-space:nowrap}
</style>
</head>
<body>
<main class="sheet">

  <section class="stats">
    <div class="stats__photo" role="img" aria-label="Photo of clenched fists breaking free from handcuffs over a table"></div>
    <h1 class="abs title title--main">DWI ARREST?</h1>
    <p class="abs title title--sub">FIGHT BACK</p>

    <svg class="abs county" width="340" height="284" viewBox="0 0 340 284" role="img" aria-label="Simplified county outline in gold">
      <polygon points="0,0 230,0 330,82 285,232 150,284 0,284" fill="var(--gold)"/>
    </svg>
    <h2 class="abs county__heading">Total Number of DWI Arrests in Marlow Parish</h2>

    <div class="abs" style="left:33px;top:288px">
      <div class="big">4,870</div>
      <div class="label" style="margin-top:4px">total DWI<br><b>arrests</b> in<br>2016*</div>
      <div class="muted" style="margin-top:6px">approx.<br>406/mo.</div>
    </div>
    <div class="abs" style="left:172px;top:288px">
      <div class="big">50%</div>
      <div class="label" style="margin-top:4px;color:var(--ink)">of the total<br>involved a<br><b>blood draw</b></div>
    </div>
    <div class="abs art" role="img" aria-label="Illustration of handcuffs, a bottle, a key and a syringe"></div>
    <p class="abs source">Information obtained from the Marlow Parish District Attorney's Office</p>
    <p class="abs asterisk">* From january to november</p>

    <p class="abs intro">In <b>2016</b>*, arrests were made for the following types of <strong>DWI related offenses:</strong></p>

    <div class="abs badge" style="left:344px;top:328px">approx.<b>184</b>month</div>
    <p class="abs stat" style="left:400px;top:326px;width:150px"><b>2,210</b> arrests for a first DWI offense<small>(including charges for a 1st DWI, open container DWI and DWI with a BAC of .15 or greater)</small></p>
    <div class="abs badge" style="left:344px;top:412px">approx.<b>60</b>month</div>
    <p class="abs stat" style="left:400px;top:416px;width:150px"><b>719</b> arrests for a second DWI offense</p>

    <div class="abs divider"></div>

    <div class="abs badge" style="left:575px;top:255px">approx.<b>34</b>month</div>
    <p class="abs stat" style="left:632px;top:258px;width:190px"><b>408</b> arrests for a third or subsequent DWI offense</p>
    <div class="abs badge" style="left:575px;top:308px">approx.<b>8</b>month</div>
    <p class="abs stat" style="left:632px;top:310px;width:190px"><b>93</b> arrests for any DWI with a child passenger under the age of 15 years old</p>
    <div class="abs badge" style="left:575px;top:360px">approx.<b>3</b>month</div>
    <p class="abs stat" style="left:632px;top:364px;width:190px"><b>31</b> arrests for a charge of intoxication assault</p>
    <div class="abs badge" style="left:575px;top:410px">approx.<b>1</b>month</div>
    <p class="abs stat" style="left:632px;top:416px;width:190px"><b>11</b> arrests for intoxication manslaughter</p>
  </section>

  <section class="effects">
    <h2 class="abs effects__heading">If you are found guilty of a DWI, your life may be affected <span>with one or more of the following:</span></h2>
    <div class="abs gavel" role="img" aria-label="Illustration of a hand holding a striking gavel"></div>

    <div class="abs item" style="left:33px;top:112px;width:172px">
      <p><b>Permanent criminal record</b> could impact your current and future employment</p>
      <svg class="icon" viewBox="0 0 36 36"><circle cx="18" cy="18" r="16" fill="none" stroke="#222" stroke-width="2"/><path d="M11 18a7 7 0 0 1 14 0M14 22a4 4 0 0 1 8 0" fill="none" stroke="#222" stroke-width="2"/></svg>
    </div>
    <div class="abs item" style="left:218px;top:112px;width:172px">
      <p><b>A driver's license suspension</b> from 6 months to 2 years on average</p>
      <svg class="icon" viewBox="0 0 36 36"><rect x="5" y="9" width="26" height="18" rx="2" fill="none" stroke="#222" stroke-width="2"/><path d="M9 15h8M9 20h10M22 14h5v6h-5z" stroke="#222" stroke-width="2" fill="none"/><path d="M3 3l30 30" stroke="#222" stroke-width="1.5"/></svg>
    </div>
    <div class="abs item" style="left:403px;top:112px;width:185px">
      <p><b>High fines</b> you will be required to pay based on your own case details</p>
      <svg class="icon" viewBox="0 0 36 36"><circle cx="18" cy="18" r="16" fill="none" stroke="#222" stroke-width="2"/><text x="18" y="25" text-anchor="middle" font-size="20" font-weight="700" fill="#222" font-family="Open Sans, sans-serif">$</text></svg>
    </div>
    <div class="abs item" style="left:605px;top:112px;width:200px">
      <p>Installation of an <b>Ignition Interlock Device system</b> in your vehicle for an average of 1 to 3 years <b>at your expense</b></p>
      <svg class="icon" viewBox="0 0 36 36"><circle cx="18" cy="18" r="16" fill="#222"/><rect x="10" y="14" width="16" height="8" rx="4" fill="none" stroke="#fff" stroke-width="2.5" transform="rotate(-45 18 18)"/></svg>
    </div>

    <div class="abs item" style="left:33px;top:210px;width:172px">
      <p>Requirement to take <b>DWI classes and/or counseling</b> before any drivers license reinstatement</p>
      <svg class="icon" viewBox="0 0 36 36"><circle cx="18" cy="18" r="16" fill="none" stroke="#222" stroke-width="2"/><rect x="10" y="12" width="16" height="12" fill="none" stroke="#222" stroke-width="2"/></svg>
    </div>
    <div class="abs item" style="left:218px;top:210px;width:172px">
      <p><b>Paying much higher insurance rates</b>, or losing your coverage entirely</p>
      <svg class="icon" viewBox="0 0 36 36"><circle cx="18" cy="18" r="16" fill="none" stroke="#222" stroke-width="2"/><text x="18" y="24" text-anchor="middle" font-size="15" font-weight="700" fill="#222" font-family="Open Sans, sans-serif">%</text></svg>
    </div>
    <div class="abs item" style="left:403px;top:210px;width:140px">
      <p><b>Travel restrictions</b> and <b>Community services</b></p>
      <svg class="icon" viewBox="0 0 36 36"><path d="M4 6l8 8M12 6l-8 8M4 26l4 4 6-8" stroke="#555" stroke-width="2" fill="none"/><rect x="18" y="6" width="14" height="10" fill="#222"/><rect x="18" y="22" width="14" height="3" fill="#222"/></svg>
    </div>
    <div class="abs item" style="left:560px;top:210px;width:90px">
      <p><b>Jail time</b></p>
      <svg class="icon" viewBox="0 0 36 36"><circle cx="18" cy="18" r="16" fill="none" stroke="#222" stroke-width="2"/><path d="M12 6v24M18 4v28M24 6v24" stroke="#222" stroke-width="2"/></svg>
    </div>
    <div class="abs item" style="left:662px;top:210px;width:143px">
      <p><b>Social stigma and hardship</b> on family and friends</p>
      <svg class="icon" viewBox="0 0 36 36"><circle cx="18" cy="18" r="8" fill="none" stroke="#222" stroke-width="2"/><circle cx="18" cy="18" r="15" fill="none" stroke="#222" stroke-width="1.5" stroke-dasharray="4 3"/></svg>
    </div>
  </section>

  <section class="cta">
    <div class="abs cta__photo" role="img" aria-label="Dim photo of scales of justice and a desk telephone keypad"></div>
    <h2 class="abs cta__headline">Hiring a quality <strong>criminal defense lawyer</strong> is probably the single <strong>most important decision</strong> you can make.</h2>
    <div class="abs logo"><span>BRANDT &amp; OKAFOR</span><i></i></div>

    <div class="abs point" style="top:35px">
      <svg width="24" height="24" viewBox="0 0 24 24"><path d="M2 9L12 3l10 6zM4 10h16v2H4zM5 13h2v6H5zM11 13h2v6h-2zM17 13h2v6h-2zM3 20h18v2H3z" fill="#fff"/></svg>
      <span>FORMER<br>PROSECUTORS</span>
    </div>
    <div class="abs point" style="top:100px">
      <svg width="24" height="24" viewBox="0 0 24 24"><polygon points="12,2 15,9 22,9 16.5,13.5 18.5,21 12,16.5 5.5,21 7.5,13.5 2,9 9,9" fill="none" stroke="#fff" stroke-width="2"/></svg>
      <span>TRIAL<br>EXPERIENCE</span>
    </div>
    <div class="abs point" style="top:165px">
      <svg width="24" height="24" viewBox="0 0 24 24"><path d="M4 3h16v12l-8 7-8-7z" fill="none" stroke="#fff" stroke-width="2"/><text x="12" y="15" text-anchor="middle" font-size="11" font-weight="700" fill="#fff" font-family="Open Sans, sans-serif">$</text></svg>
      <span>FAIR FEE</span>
    </div>

    <p class="abs call">Call to speak to an experienced attorney now. <b>The sooner you call, the sooner we can help</b>.</p>
    <p class="abs phone">555-013-7200</p>
    <p class="abs email">dwi@brandt-okafor.example</p>
  </section>

</main>
</body>
</html>
```